Book Cover " FROM CINDERBLOCK TO TARN"

Looking for a book cover for a novel FROM CINDERBLOCK TO TARN.
Tarn is the characters developed name. The book describes his rough up bringing and how he obtains his greatness and his given name Tarn.

```html
<!DOCTYPE html>
<html lang="en">
<head>
<meta charset="utf-8">
<title>From Cinderblock to Tarn — Book Cover</title>
<link href="https://fonts.googleapis.com/css2?family=Barlow+Condensed:wght@700&display=swap" rel="stylesheet">
<style>
  :root {
    --page-bg: #ececec;
    --silk-deep: #1c0203;
    --silk-mid: #4e0506;
    --silk-bright: #9a0f0d;
    --coral-light: #f4857a;
    --coral-mid: #d85a50;
    --coral-dark: #8f2222;
    --gold-dark: #a18a2a;
    --gold-cream: #fbf3dc;
    --roll-light: #6e3f3d;
    --roll-dark: #3a1a1a;
  }
  * { margin: 0; padding: 0; box-sizing: border-box; }
  html, body {
    width: 720px;
    height: 1200px;
    overflow: hidden;
    background: var(--page-bg);
  }
  .cover {
    position: absolute;
    left: 0;
    top: 60px;
    width: 720px;
    height: 1080px;
    overflow: hidden;
    font-family: "Barlow Condensed", "Arial Narrow", sans-serif;
    font-weight: 700;
    text-transform: uppercase;
  }
  .cover__silk {
    position: absolute;
    inset: 0;
    background: linear-gradient(180deg,
      var(--silk-mid) 0%,
      var(--silk-deep) 30%,
      var(--silk-deep) 55%,
      var(--silk-mid) 75%,
      var(--silk-bright) 100%);
  }
  .cover__rolls {
    position: absolute;
    left: 40px;
    top: 566px;
    width: 476px;
    height: 350px;
    border-radius: 18px;
    background: linear-gradient(160deg, var(--roll-light) 0%, var(--roll-dark) 100%);
  }
  .title {
    position: absolute;
    left: 84px;
    top: 70px;
    line-height: 0.86;
  }
  .title__line { display: block; white-space: nowrap; }
  .title__word {
    display: inline-block;
    background-clip: text;
    -webkit-background-clip: text;
    color: transparent;
    filter: drop-shadow(4px 5px 3px rgba(20, 0, 0, 0.55));
  }
  .title__word--coral {
    background-image: linear-gradient(180deg, var(--coral-light) 0%, var(--coral-mid) 50%, var(--coral-dark) 100%);
  }
  .title__word--gold {
    background-image: linear-gradient(180deg, var(--gold-dark) 0%, var(--gold-cream) 50%, var(--gold-dark) 100%);
  }
  .title__from { font-size: 206px; }
  .title__middle { font-size: 114px; margin-top: 8px; }
  .title__final { margin-top: 0; display: flex; align-items: flex-start; gap: 18px; }
  .title__to { font-size: 170px; }
  .title__name { font-size: 224px; }
</style>
</head>
<body>
  <main class="cover">
    <div class="cover__silk" role="img" aria-label="Draped deep red silk fabric filling the background"></div>
    <div class="cover__rolls" role="img" aria-label="Two rolls of worn sandpaper tied with gold twine resting on the silk"></div>
    <h1 class="title">
      <span class="title__line"><span class="title__word title__word--coral title__from">From</span></span>
      <span class="title__line"><span class="title__word title__word--gold title__middle">Cinderblock</span></span>
      <span class="title__line title__final">
        <span class="title__word title__word--gold title__to">To</span>
        <span class="title__word title__word--coral title__name">Tarn</span>
      </span>
    </h1>
  </main>
</body>
</html>
```